German Headhunter/ HR Consultancy needs Business Cards Design

We need a business Card Design for our Company in Stuttgart. We are specialized as Headhunter/ HR Consultancy in Placement of specialist and managers in permanent employment. Please refer to our business logo.

```html
<!DOCTYPE html>
<html lang="de">
<head>
<meta charset="utf-8">
<title>Kernwerk Personalberatung – Visitenkarten</title>
<link href="https://fonts.googleapis.com/css2?family=Arimo:wght@400;700&display=swap" rel="stylesheet">
<style>
  :root {
    --brand-blue: #3a55a6;
    --accent-grey: #9a9b9f;
    --rule-grey: #a9a9a9;
    --ink: #1e1e1e;
    --paper: #ffffff;
    --backdrop: #e9e9eb;
  }
  * { box-sizing: border-box; margin: 0; padding: 0; }
  html, body {
    width: 1200px; height: 900px; overflow: hidden;
    background: var(--backdrop);
    font-family: "Arimo", Arial, sans-serif;
  }
  .sheet {
    position: relative; width: 1200px; height: 900px;
  }
  .card {
    position: absolute; left: 250px; width: 700px; height: 400px;
    box-shadow: 0 6px 18px rgba(0,0,0,0.12);
    overflow: hidden;
  }
  /* Front */
  .card--front { top: 35px; background: var(--brand-blue); }
  .front-brand {
    position: absolute; left: 50%; top: 50%;
    transform: translate(-50%, -50%);
    display: flex; align-items: center; gap: 26px;
    color: var(--paper); font-weight: 700;
  }
  .brand-square {
    width: 62px; height: 62px; background: var(--paper);
  }
  .front-brand .brand-name { font-size: 54px; letter-spacing: 3px; line-height: 1; }
  .front-brand .brand-sub { font-size: 22px; letter-spacing: 2.5px; margin-top: 6px; }

  /* Back */
  .card--back { top: 465px; background: var(--paper); }
  .back-brand {
    position: absolute; left: 60px; top: 58px;
    display: flex; align-items: center; gap: 16px;
    color: var(--brand-blue); font-weight: 700;
  }
  .back-brand .brand-square { width: 40px; height: 40px; background: var(--brand-blue); }
  .back-brand .brand-name { font-size: 34px; letter-spacing: 2px; line-height: 1; }
  .back-brand .brand-sub { font-size: 14px; letter-spacing: 1.6px; margin-top: 4px; }

  .person {
    position: absolute; right: 60px; top: 62px; text-align: right;
  }
  .person__name {
    font-weight: 700; font-size: 30px; color: var(--brand-blue); letter-spacing: 0.5px;
  }
  .person__role { font-size: 15px; color: var(--ink); margin-top: 6px; }

  .divider {
    position: absolute; left: 60px; right: 140px; top: 178px;
    height: 1.5px; background: var(--rule-grey);
  }

  .contact {
    position: absolute; left: 60px; top: 198px;
    font-size: 17px; color: var(--ink); line-height: 1.45;
    list-style: none;
  }
  .contact__item { display: flex; align-items: center; gap: 10px; }
  .contact__item--plain { padding-left: 0; }
  .contact__icon { width: 18px; height: 18px; flex: none; }

  .band { position: absolute; bottom: 0; left: 0; width: 700px; height: 40px; }
</style>
</head>
<body>
<main class="sheet">

  <section class="card card--front" aria-label="Visitenkarte Vorderseite">
    <div class="front-brand">
      <span class="brand-square"></span>
      <div class="brand-text">
        <div class="brand-name">KERNWERK</div>
        <div class="brand-sub">PERSONALBERATUNG</div>
      </div>
    </div>
  </section>

  <section class="card card--back" aria-label="Visitenkarte Rückseite">
    <div class="back-brand">
      <span class="brand-square"></span>
      <div class="brand-text">
        <div class="brand-name">KERNWERK</div>
        <div class="brand-sub">PERSONALBERATUNG</div>
      </div>
    </div>

    <div class="person">
      <div class="person__name">JONAS FELDMANN</div>
      <div class="person__role">CEO/Founder</div>
    </div>

    <div class="divider"></div>

    <ul class="contact">
      <li class="contact__item--plain">2315 Marlow Street</li>
      <li class="contact__item--plain">Unit B Country Name, 5120</li>
      <li class="contact__item">
        <svg class="contact__icon" viewBox="0 0 18 18" aria-hidden="true">
          <circle cx="9" cy="9" r="9" fill="var(--brand-blue)"/>
          <path d="M6 4.5c-1 .6-1.3 1.6-.9 2.8.8 2.3 2.4 4 4.6 5 1.1.5 2.2.2 2.8-.8l-1.7-1.5-1 .7c-1-.5-1.9-1.4-2.4-2.4l.7-1z" fill="#fff"/>
        </svg>
        (555) 180 - 2264
      </li>
      <li class="contact__item">
        <svg class="contact__icon" viewBox="0 0 18 18" aria-hidden="true">
          <rect x="1.5" y="4" width="15" height="10" fill="var(--brand-blue)"/>
          <path d="M1.5 4l7.5 6 7.5-6" fill="none" stroke="#fff" stroke-width="1.2"/>
        </svg>
        info@kernwerkpersonal.com
      </li>
      <li class="contact__item">
        <svg class="contact__icon" viewBox="0 0 18 18" aria-hidden="true">
          <circle cx="9" cy="9" r="8" fill="var(--brand-blue)"/>
          <ellipse cx="9" cy="9" rx="3.5" ry="8" fill="none" stroke="#fff" stroke-width="1"/>
          <line x1="1" y1="9" x2="17" y2="9" stroke="#fff" stroke-width="1"/>
        </svg>
        www.kernwerkpersonal.com
      </li>
    </ul>

    <svg class="band" viewBox="0 0 700 40" aria-hidden="true">
      <polygon points="0,28 470,28 482,40 0,40" fill="var(--brand-blue)"/>
      <polygon points="478,0 700,0 700,40 510,40" fill="var(--accent-grey)"/>
    </svg>
  </section>

</main>
</body>
</html>
```